wooden jewelry - pearl necklaces

I sell wooden jeweler (rings and pearls) on markets, and so on. I also opened my business as a carpenter. The rings and a combination of wood and metal. The wood is special wood, not very common on Europe. I paint the rings afterwards. You can see some of the pictures on the pictures I uploaded. The pearls are made of the same kind of wood and colored in all kinds of colors. They are then assembled to bracelets. The jewelry is very individual and looks really cool and all kinds of people.

Target Market(s)

Young urban alternative with a sense of individuality

Contact Information for Business Card

Front:

Text:

„Kugelwerk“ (big)
„Malte Oswitz“ (smaler)

Back
„Holzschmuck
Herstellung von individuellem Holz- und Modeschmuck

Malte Oswitz
Tel: 015239460518
Lindgarbweg 9
83127 Burghausen

malteoswitz@postfeld.de“

Font styles to use
Sans Serif

Requirements
Nice to have
• Nice to see a camel thorn tree on the background, this is a special wood and some of the rings are made out of this wood.

```html
<!DOCTYPE html>
<html lang="de">
<head>
<meta charset="utf-8">
<title>Kugelwerk – Visitenkarte</title>
<link rel="stylesheet" href="https://fonts.googleapis.com/css2?family=Great+Vibes&family=Cinzel:wght@400&family=Arimo:wght@400&display=swap">
<style>
  :root {
    --stage: #e9e6e2;
    --card-black: #000000;
    --ring-grey: #8a8a8a;
    --logo-grey: #a9a9a9;
    --gold: #d9a85a;
    --white: #ffffff;
    --bead-dark: #3a1f24;
    --bead-mid: #8a4a2a;
    --bead-light: #e2c28a;
    --bead-red: #b8263a;
  }
  * { margin: 0; padding: 0; box-sizing: border-box; }
  html, body { width: 1200px; height: 900px; overflow: hidden; background: var(--stage); }
  .canvas { position: relative; width: 1200px; height: 900px; }

  .card {
    position: absolute; left: 260px; width: 680px; height: 388px;
    border-radius: 22px; overflow: hidden;
    box-shadow: 0 6px 18px rgba(0,0,0,0.25);
  }
  .card--front { top: 42px; }
  .card--back { top: 470px; }

  .bead-photo {
    position: absolute; inset: 0;
    background:
      radial-gradient(circle at 20% 30%, var(--bead-light) 0, transparent 22%),
      radial-gradient(circle at 70% 20%, var(--bead-red) 0, transparent 14%),
      radial-gradient(circle at 80% 75%, var(--bead-light) 0, transparent 20%),
      radial-gradient(circle at 35% 80%, var(--bead-mid) 0, transparent 22%),
      linear-gradient(135deg, var(--bead-dark), var(--bead-mid) 45%, var(--bead-light) 70%, var(--bead-dark));
  }

  /* front */
  .emblem {
    position: absolute; left: 50%; top: 50%; width: 250px; height: 250px;
    transform: translate(-50%, -50%); border-radius: 50%;
    background: var(--card-black);
    display: flex; align-items: center; justify-content: center;
  }
  .emblem::after {
    content: ""; position: absolute; inset: 10px; border-radius: 50%;
    border: 1px solid var(--ring-grey);
  }
  .brand {
    font-family: "Cinzel", serif; color: var(--logo-grey);
    font-size: 24px; letter-spacing: 1px; display: flex; align-items: center; gap: 10px;
  }
  .brand__dot { width: 12px; height: 12px; border-radius: 50%; background: var(--logo-grey); }

  /* back */
  .info-band {
    position: absolute; left: 0; right: 0; top: 46px; height: 270px;
    background: var(--card-black);
  }
  .info-band .brand { position: absolute; left: 60px; top: 112px; font-size: 26px; }
  .holder-name {
    position: absolute; right: 80px; top: 18px;
    font-family: "Great Vibes", cursive; color: var(--gold); font-size: 50px;
  }
  .contact-list {
    position: absolute; right: 60px; top: 100px; list-style: none;
    font-family: "Arimo", sans-serif; color: var(--white); font-size: 15px; line-height: 1.35;
  }
  .contact-list li { display: flex; justify-content: flex-end; align-items: flex-start; gap: 12px; margin-bottom: 6px; text-align: right; }
  .contact-list svg { flex: none; margin-top: 2px; }
  .trade-line {
    position: absolute; right: 110px; top: 205px;
    font-family: "Great Vibes", cursive; color: var(--gold); font-size: 40px;
  }
</style>
</head>
<body>
<main class="canvas">

  <section class="card card--front">
    <div class="bead-photo" role="img" aria-label="Foto: bunte Holzperlen in Rot, Braun, Violett und Naturtönen"></div>
    <div class="emblem">
      <div class="brand"><span class="brand__dot"></span>Kugelwerk</div>
    </div>
  </section>

  <section class="card card--back">
    <div class="bead-photo" role="img" aria-label="Foto: bunte Holzperlen in Rot, Braun, Violett und Naturtönen"></div>
    <div class="info-band">
      <div class="brand"><span class="brand__dot"></span>Kugelwerk</div>
      <div class="holder-name">Malte Oswitz</div>
      <ul class="contact-list">
        <li>015239460518
          <svg width="12" height="16" viewBox="0 0 12 16"><rect x="1" y="1" width="10" height="14" rx="2" fill="none" stroke="var(--gold)" stroke-width="1.6"/><circle cx="6" cy="12.5" r="1" fill="var(--gold)"/></svg>
        </li>
        <li>malteoswitz@postfeld.de
          <svg width="16" height="12" viewBox="0 0 16 12"><rect x="0" y="0" width="16" height="12" rx="1" fill="var(--gold)"/><path d="M1 1 L8 7 L15 1" fill="none" stroke="var(--card-black)" stroke-width="1.3"/></svg>
        </li>
        <li>Lindgarbweg 9<br>83127 Burghausen
          <svg width="12" height="16" viewBox="0 0 12 16"><path d="M6 15 C2 10 0 7.5 0 5.5 A6 6 0 0 1 12 5.5 C12 7.5 10 10 6 15 Z" fill="var(--gold)"/><circle cx="6" cy="5.5" r="2" fill="var(--card-black)"/></svg>
        </li>
      </ul>
      <div class="trade-line">Wooden Jewelry</div>
    </div>
  </section>

</main>
</body>
</html>
```